Business Card Design Project - IT Company

Kestrafield Information Technology Solutions
We are an Information Technology Company. We provide computer services to commercial companies. We would like a new card full color front and back with bleeding edge.
We have a logo that you can use or if you want to come up with a new logo that is fine too.
Our colors are mostly Maroon and black but be creative.
Sample Information
Brent R Okafor
4812 W Saguaro Ridge Drive
Suite 410
Phoenix, AZ 85027
O: 602.914.2037
C: 602.468.1290
24/7: 888.914.2037
bokafor@kestrafield.example
www.kestrafield.example
Target Market(s)
Business of all sizes
Industry/Entity Type
Computer
Requirements
Must have
- Bleeding edge
full color on both sides

```html
<!DOCTYPE html>
<html lang="en">
<head>
<meta charset="utf-8">
<title>Kestrafield Business Card</title>
<link rel="stylesheet" href="https://fonts.googleapis.com/css2?family=Arimo:wght@400;700&display=swap">
<style>
  :root {
    --stage: #1c0d0d;
    --card-top: #333333;
    --card-bottom: #1f1f1f;
    --maroon: #c42323;
    --maroon-deep: #8e1414;
    --white: #ffffff;
    --soft-white: #e6e6e6;
    --grey: #9a9a9a;
  }
  * { margin: 0; padding: 0; box-sizing: border-box; }
  html, body {
    width: 1200px;
    height: 900px;
    overflow: hidden;
    background: var(--stage);
    font-family: "Arimo", Arial, sans-serif;
  }
  .sheet {
    position: relative;
    width: 1200px;
    height: 900px;
  }
  .card {
    position: absolute;
    left: 250px;
    width: 700px;
    height: 400px;
    overflow: hidden;
    background: linear-gradient(160deg, var(--card-top), var(--card-bottom));
    box-shadow: 0 10px 30px rgba(0, 0, 0, 0.6);
  }
  .card--front { top: 40px; }
  .card--back { top: 470px; }

  .swoosh {
    position: absolute;
    inset: 0;
    width: 100%;
    height: 100%;
  }

  .holder-name {
    position: absolute;
    top: 36px;
    right: 50px;
    font-size: 52px;
    font-weight: 400;
    color: var(--white);
    letter-spacing: 0.5px;
    white-space: nowrap;
  }
  .holder-name__first { color: var(--maroon); }

  .phone-line {
    position: absolute;
    top: 108px;
    right: 50px;
    font-size: 16px;
    font-weight: 700;
    color: var(--white);
    white-space: nowrap;
  }
  .phone-line .label { color: var(--maroon); }

  .support-line {
    position: absolute;
    top: 134px;
    right: 50px;
    font-size: 28px;
    color: var(--white);
    white-space: nowrap;
  }
  .support-line .label { color: var(--maroon); font-weight: 700; }

  .divider {
    position: absolute;
    top: 196px;
    right: 50px;
    width: 250px;
    height: 2px;
    background: linear-gradient(90deg, transparent, var(--grey));
  }

  .address {
    position: absolute;
    top: 216px;
    right: 50px;
    text-align: right;
    font-style: normal;
    font-size: 18px;
    line-height: 1.35;
    color: var(--soft-white);
    white-space: nowrap;
  }

  .web-contact {
    position: absolute;
    left: 36px;
    bottom: 36px;
    font-size: 19px;
    line-height: 1.35;
    color: var(--white);
    white-space: nowrap;
  }

  .brand {
    position: absolute;
    left: 0;
    right: 0;
    top: 128px;
    text-align: center;
  }
  .brand__name {
    font-size: 66px;
    font-weight: 700;
    letter-spacing: 6px;
    text-transform: uppercase;
    color: var(--soft-white);
  }
  .brand__tagline {
    margin-top: 6px;
    font-size: 17px;
    font-weight: 700;
    letter-spacing: 2.5px;
    color: var(--soft-white);
  }

  .base-rule {
    position: absolute;
    left: 0;
    right: 0;
    top: 345px;
    height: 4px;
    display: flex;
  }
  .base-rule__light { flex: 0 0 82%; background: var(--soft-white); }
  .base-rule__accent { flex: 1; background: var(--maroon); }
</style>
</head>
<body>
<main class="sheet">

  <section class="card card--front" aria-label="Card front">
    <svg class="swoosh" viewBox="0 0 700 400" aria-hidden="true">
      <defs>
        <linearGradient id="redFill" x1="0" y1="0" x2="1" y2="1">
          <stop offset="0" stop-color="#d42a2a"/>
          <stop offset="1" stop-color="#8e1414"/>
        </linearGradient>
      </defs>
      <path d="M0,124 C140,112 205,195 295,266 S430,384 480,400 L0,400 Z" fill="url(#redFill)"/>
      <path d="M0,112 C150,98 215,185 305,256 S440,378 500,400" fill="none" stroke="#f2f2f2" stroke-width="5"/>
    </svg>

    <h1 class="holder-name"><span class="holder-name__first">Brent</span> R Okafor</h1>
    <p class="phone-line"><span class="label">O:</span> 602.914.2037 / <span class="label">C:</span> 602.468.1290</p>
    <p class="support-line"><span class="label">24/7:</span> 888.914.2037</p>
    <div class="divider"></div>
    <address class="address">
      4812 W Saguaro Ridge Drive<br>
      Suite 410<br>
      Phoenix, AZ 85027
    </address>
    <p class="web-contact">
      bokafor@kestrafield.example<br>
      www.kestrafield.example
    </p>
  </section>

  <section class="card card--back" aria-label="Card back">
    <div class="brand">
      <p class="brand__name">Kestrafield</p>
      <p class="brand__tagline">Information Technology Solutions</p>
    </div>
    <div class="base-rule">
      <span class="base-rule__light"></span>
      <span class="base-rule__accent"></span>
    </div>
  </section>

</main>
</body>
</html>
```